Torvela Lighting needs a new website (only informative)

Torvela Lighting (Pty) Ltd imports and distributes LED lighting products to South Africa. Our existing website (www.torvela.co.za) is designed and implemented on a shopping cart template: Pix-Basket.

The website needs to be redesigned. It should no longer be based on a shopping cart template, but purely informative and allow some PDF downloads. It should scale well and allow quick & easy changes by the website owner: Including adding, changing and removing products. Other information pages should also be easy to manage.

No need to design a logo. A logo and user requirement specification is uploaded with more details.

Target Market(s)

Retailers, interior designers, architects, contractors, electricians, franchises etc. with a need for energy efficient LED lighting.

Industry/Entity Type

Shopping

Font styles to use
Sans Serif

Colors
0355a3
0892cd
86cae6
86cfc6

Requirements
Must have
• Existing logo to be used.
All pages informative & PDF download capability.
User friendly management
SEO capability

```html
<!DOCTYPE html>
<html lang="en">
<head>
<meta charset="utf-8">
<title>Torvela Lighting</title>
<link href="https://fonts.googleapis.com/css2?family=Baloo+2:wght@600&family=Signika:wght@300&family=Open+Sans:wght@400;600&display=swap" rel="stylesheet">
<style>
:root{
  --brand:#14587a;
  --brand-dark:#0f4a69;
  --band-top:#1a6b94;
  --band-bottom:#0f5579;
  --accent:#0892cd;
  --ink:#222;
  --panel:#f2f2f2;
  --footer-top:#4a4a4a;
  --footer-bottom:#2b2b2b;
  --footer-text:#c9c9c9;
}
*{box-sizing:border-box;margin:0;padding:0}
html,body{width:1133px;height:1200px;overflow:hidden;background:#fff}
body{font-family:Arial,Helvetica,sans-serif;color:var(--ink);position:relative}
a{text-decoration:none;color:inherit}
.abs{position:absolute}

/* header */
.brand{left:110px;top:34px;font-family:"Baloo 2",sans-serif;font-size:40px;line-height:1;color:var(--brand)}
.brand-sub{left:165px;top:78px;font-family:"Baloo 2",sans-serif;font-size:14px;letter-spacing:3px;color:var(--brand)}
.util{font-family:"Open Sans",sans-serif;font-size:12px;color:#333;display:flex;align-items:center;gap:5px;white-space:nowrap}
.util .note{color:var(--accent)}
.contact{left:795px;top:15px}
.downloads{left:914px;top:15px}
.country{left:893px;top:55px;font-size:11px;color:#5a4a1a}
.country-drop{left:1012px;top:55px;width:18px;height:17px;border:1px solid #ccc}
.search{left:807px;top:97px;width:228px;height:25px;border:1px solid #bbb;display:flex}
.search span{flex:1;font-family:"Open Sans",sans-serif;font-size:11px;color:#555;padding:5px 4px}
.search .go{width:25px;background:#2a7ad8;display:flex;align-items:center;justify-content:center}

/* band + nav */
.band{left:0;top:132px;width:1133px;height:461px;background:linear-gradient(var(--band-top),var(--band-bottom));border-bottom:2px solid #fff}
.nav{left:112px;top:132px;height:42px;display:flex;align-items:stretch}
.nav a{color:#fff;font-family:Arial,Helvetica,sans-serif;font-size:13px;display:flex;align-items:center;padding:0 19px;border-right:1px solid rgba(255,255,255,.15);white-space:nowrap}
.nav a:last-child{border-right:none}
.slider{left:119px;top:194px;width:890px;height:372px;border-radius:16px;background:#f4f4f4;border:3px solid #fff}
.slide{left:143px;top:219px;width:842px;height:322px;border-radius:12px;background:#fff}
.slide-img{left:160px;top:240px;width:400px;height:270px;border-radius:8px;background:radial-gradient(circle at 40% 50%,#d9d9d9,#f7f7f7 70%)}
.slide-title{left:583px;top:248px;font-family:"Baloo 2",sans-serif;font-size:40px;color:var(--brand);line-height:1.2;white-space:nowrap}
.slide-rule{left:584px;top:312px;width:370px;border-top:1px dotted #aaa}
.slide-copy{left:584px;top:330px;width:365px;font-size:12px;line-height:19px;text-align:justify;color:#222}
.slide-copy b{color:var(--brand)}
.slide-arrow{top:364px;width:48px;height:40px;background:linear-gradient(#444,#111);display:flex;align-items:center;justify-content:center}
.slide-arrow.prev{left:130px;border-radius:0 20px 20px 0}
.slide-arrow.next{left:949px;border-radius:20px 0 0 20px}
.dots{left:512px;top:522px;width:104px;height:28px;border-radius:14px;background:#fff;border:1px solid #ccc;display:flex;align-items:center;justify-content:center;gap:3px}
.dots i{width:11px;height:11px;border-radius:50%;background:#777}
.dots i:first-child{background:#fff;border:2px solid #777}

/* gallery */
.gallery{left:94px;top:628px;width:937px;height:132px;background:var(--panel);border:1px solid #ddd}
.thumb{top:642px;width:160px;height:105px;border:2px solid #fff;box-shadow:0 0 2px #aaa}
.gal-arrow{top:680px}

/* categories */
.cat-tab{top:811px;width:200px;height:36px;border-radius:8px;background:linear-gradient(#1d6a92,var(--brand-dark));color:#fff;font-family:"Signika",sans-serif;font-weight:300;font-size:19px;display:flex;align-items:center;justify-content:center;box-shadow:0 2px 2px #999;white-space:nowrap}
.cat-dome{top:855px;width:200px;height:110px;border-radius:100px 100px 0 0;background:linear-gradient(#fff,#f0f0f0);border:1px solid #e6e6e6;border-bottom:none}
.cat-img{width:80px;height:80px;border-radius:8px;left:60px;top:20px;position:absolute;background:radial-gradient(circle,#cfd6dc,#eef0f2 70%)}
.cat-copy{top:976px;width:192px;font-family:Arial,Helvetica,sans-serif;font-size:11px;line-height:17px;text-align:justify;letter-spacing:.3px;color:#222}
.cat-more{top:1044px;width:192px;text-align:right;font-family:Arial,Helvetica,sans-serif;font-size:11px;letter-spacing:.3px;color:#333}
.sep{top:828px;height:237px;border-left:1px dotted #777}

/* footer */
.footer{left:0;top:1097px;width:1133px;height:103px;background:linear-gradient(var(--footer-top),var(--footer-bottom))}
.foot-brand{left:102px;top:1118px;font-family:"Baloo 2",sans-serif;font-size:36px;line-height:1;color:#bdbdbd}
.foot-links{left:337px;top:1142px;font-family:Arial,Helvetica,sans-serif;font-size:10px;color:var(--footer-text);white-space:nowrap}
.foot-copy{left:362px;top:1175px;font-family:Arial,Helvetica,sans-serif;font-size:11px;color:#999;white-space:nowrap}
.foot-copy span{color:#ccc;font-size:12px}
.social{left:865px;top:1122px;display:flex;gap:5px}
.social i{width:31px;height:31px;border-radius:50%;background:#c8c8c8}
</style>
</head>
<body>
<header>
  <div class="abs brand">Torvela</div>
  <div class="abs brand-sub">LED LIGHTS</div>
  <a class="abs util contact" href="#"><svg width="14" height="14" viewBox="0 0 14 14"><rect x="1" y="3" width="12" height="8" fill="none" stroke="#555" stroke-width="1.4"/><path d="M1 3l6 5 6-5" fill="none" stroke="#555" stroke-width="1.4"/></svg>Contact Us</a>
  <a class="abs util downloads" href="#"><svg width="12" height="14" viewBox="0 0 12 14"><path d="M1 1h7l3 3v9H1z" fill="none" stroke="#555" stroke-width="1.4"/><path d="M6 5v5M4 8l2 2 2-2" fill="none" stroke="#555" stroke-width="1.3"/></svg>Downloads <span class="note">(PDF)</span></a>
  <div class="abs util country"><svg width="30" height="14" viewBox="0 0 30 14"><ellipse cx="8" cy="7" rx="7" ry="5" fill="#7bbf4e"/><ellipse cx="22" cy="6" rx="8" ry="5" fill="#7bbf4e"/></svg>Select Country</div>
  <div class="abs country-drop"><svg width="16" height="15" viewBox="0 0 16 15"><path d="M5 6h6l-3 4z" fill="#d00"/></svg></div>
  <div class="abs search"><span>Site Search</span><div class="go"><svg width="12" height="12" viewBox="0 0 12 12"><circle cx="5" cy="5" r="3.5" fill="none" stroke="#fff" stroke-width="1.8"/><path d="M7.5 7.5l3.5 3.5" stroke="#fff" stroke-width="2"/></svg></div></div>
</header>

<div class="abs band"></div>
<nav class="abs nav">
  <a href="#"><svg width="13" height="12" viewBox="0 0 13 12"><path d="M6.5 0L0 6h2v6h3.5V8h2v4H11V6h2z" fill="#fff"/></svg></a>
  <a href="#">LED down lights</a><a href="#">LED bulbs</a><a href="#">LED tube lights</a><a href="#">Dimmable LED lamps</a><a href="#">Flood Lights</a><a href="#">LED strip lights</a><a href="#">Other LED lights</a>
</nav>

<section>
  <div class="abs slider"></div>
  <div class="abs slide"></div>
  <div class="abs slide-img" role="img" aria-label="Two finned LED spotlight bulbs, side and front view"></div>
  <h1 class="abs slide-title">Torvela Led Lights</h1>
  <div class="abs slide-rule"></div>
  <p class="abs slide-copy"><b>Lorem ipsum dolor sit amet, etiam sit rhoncus iaculis facilisis curabitur,</b> orci malesuada. Vitae placerat justo eu, arcu justo leo. Purus enim hendrerit nunc praesent enim vivamus, nulla adipiscing quam vestibulum class vel justo, a elit justo urna dolor, quisque orci lacus venenatis a vivamus. Duis turpis risus pede enim facilisi.<br><br>Cursus bibendum velit turpis sed, dui curabitur. Velit condimentum integer, egestas tempor...</p>
  <div class="abs slide-arrow prev"><svg width="14" height="16" viewBox="0 0 14 16"><path d="M3 2l7 6-7 6" fill="none" stroke="#fff" stroke-width="3"/></svg></div>
  <div class="abs slide-arrow next"><svg width="14" height="16" viewBox="0 0 14 16"><path d="M11 2L4 8l7 6" fill="none" stroke="#fff" stroke-width="3"/></svg></div>
  <div class="abs dots"><i></i><i></i><i></i><i></i><i></i></div>
</section>

<section>
  <div class="abs gallery"></div>
  <svg class="abs gal-arrow" style="left:107px" width="14" height="28" viewBox="0 0 14 28"><path d="M12 2L2 14l10 12z" fill="#888"/></svg>
  <svg class="abs gal-arrow" style="left:1005px" width="14" height="28" viewBox="0 0 14 28"><path d="M2 2l10 12L2 26z" fill="#888"/></svg>
  <div class="abs thumb" style="left:133px;background:linear-gradient(#7a4a1e,#e0a05a)" role="img" aria-label="Row of warm wall lights"></div>
  <div class="abs thumb" style="left:308px;background:linear-gradient(#c9b59a,#8a6e55)" role="img" aria-label="Lit living room interior"></div>
  <div class="abs thumb" style="left:482px;background:linear-gradient(#2a2a35,#8a6a45)" role="img" aria-label="House exterior lit at dusk"></div>
  <div class="abs thumb" style="left:656px;background:linear-gradient(#e4e4e4,#9c9890)" role="img" aria-label="Open plan lounge with ceiling lights"></div>
  <div class="abs thumb" style="left:831px;background:linear-gradient(#d8d4cc,#6d6a66)" role="img" aria-label="Dining room with recessed lighting"></div>
</section>

<section>
  <div class="abs cat-tab" style="left:107px">LED down lights</div>
  <div class="abs cat-tab" style="left:341px">Dimmable LED</div>
  <div class="abs cat-tab" style="left:583px">LED strip lights</div>
  <div class="abs cat-tab" style="left:809px">Flood Lights</div>

  <div class="abs cat-dome" style="left:111px"><div class="cat-img" role="img" aria-label="LED down light bulb"></div></div>
  <div class="abs cat-dome" style="left:338px"><div class="cat-img" role="img" aria-label="Dimmable LED lamp"></div></div>
  <div class="abs cat-dome" style="left:582px"><div class="cat-img" role="img" aria-label="LED spot bulb"></div></div>
  <div class="abs cat-dome" style="left:817px"><div class="cat-img" role="img" aria-label="LED flood light"></div></div>

  <p class="abs cat-copy" style="left:116px">Quis cum nibh tellus, dapibus est duis felis id proin molestie, duis tortor amet quam amet nec...</p>
  <p class="abs cat-copy" style="left:344px">Quis cum nibh tellus, dapibus est duis felis id proin molestie, duis tortor amet quam amet nec...</p>
  <p class="abs cat-copy" style="left:585px">Quis cum nibh tellus, dapibus est duis felis id proin molestie, duis tortor amet quam amet nec...</p>
  <p class="abs cat-copy" style="left:818px">Quis cum nibh tellus, dapibus est duis felis id proin molestie, duis tortor amet quam amet nec...</p>

  <a class="abs cat-more" style="left:116px" href="#">View More [+]</a>
  <a class="abs cat-more" style="left:350px" href="#">View More [+]</a>
  <a class="abs cat-more" style="left:587px" href="#">View More [+]</a>
  <a class="abs cat-more" style="left:818px" href="#">View More [+]</a>

  <div class="abs sep" style="left:324px"></div>
  <div class="abs sep" style="left:561px"></div>
  <div class="abs sep" style="left:797px"></div>
</section>

<footer>
  <div class="abs footer"></div>
  <div class="abs foot-brand">Torvela</div>
  <div class="abs foot-links">LED down lights &nbsp;|&nbsp; LED bulbs &nbsp;|&nbsp; LED tube lights &nbsp;|&nbsp; Dimmable LED lamps &nbsp;|&nbsp; Flood Lights &nbsp;|&nbsp; LED strip lights</div>
  <div class="abs foot-copy">©2013 <span>Torvela LED</span> &nbsp; All rights reserved. &nbsp; Privacy Policy &nbsp;|&nbsp; Terms &amp; Conditions</div>
  <div class="abs social" role="img" aria-label="Social media links"><i></i><i></i><i></i><i></i><i></i></div>
</footer>
</body>
</html>
```